Roofing web site brel roofing

Look at some of our competitors web page we like something similar with NYC roofing
https://www.dovantileworks.example/
Maybe a skyline picture of nyc at the home page with a picture of flat roofing installation

Target Market(s)

Commercial and residential flat roofs

Industry/Entity Type

Flat Roofing industry

Coding

Coded - Design and coding required

Number of Pages Required

2 page

Font styles to use
Decorative
Script

Colors

Designer to choose colors to be used in the design.

Requirements
Must have
• At BREL Roofing, we are a trusted and reputable roofing company specializing in new construction flat roof installation and repair. With years of experience in the industry, we take pride in providing exceptional roofing solutions to our valued clients. Our team of highly skilled and dedicated roofing professionals understands the unique challenges and requirements of new construction projects. We work closely with builders, contractors, and architects to design and install flat roofs that meet the specific needs of each project. From commercial buildings to residential complexes, we have the expertise to deliver reliable and durable roofing solutions. When it comes to flat roof repairs, we are your go-to experts. Our experienced technicians conduct thorough inspections to identify the root cause of any issues your roof may be experiencing. We utilize the latest industry techniques and high-quality materials to efficiently repair your flat roof, ensuring its integrity and longevity. At BREL Roofing, we prioritize customer satisfaction above all else. We believe in building strong relationships with our clients by providing exceptional craftsmanship and outstanding customer service. Our team is dedicated to delivering projects on time, within budget, and to the highest standards of quality. We understand that a well-maintained roof is essential for protecting your property and ensuring the safety of its occupants. That's why we use only the best materials and employ skilled professionals who are trained in the latest roofing practices. Our commitment to excellence is evident in every project we undertake. As a fully licensed and insured roofing company, we prioritize safety and adhere to industry regulations and best practices. We take every precaution to create a safe working environment for our team and minimize any disruptions to your daily routine. When you choose BREL Roofing, you can trust that you are working with a reliable and reputable company that will deliver exceptional results. We are committed to exceeding your expectations and providing you with a roof that is built to last. Contact us today for all your new construction flat roof installation and repair needs.
Nice to have
• NYC skyline background with commercial roofing pictures of torching roofing

```html
<!DOCTYPE html>
<html lang="en">
<head>
<meta charset="utf-8">
<title>Brel Roofing</title>
<link href="https://fonts.googleapis.com/css2?family=Poppins:wght@400;500;600;700;800&family=Montserrat:wght@400;500;600;700&display=swap" rel="stylesheet">
<style>
:root{
  --orange:#f26522;
  --black:#050505;
  --white:#ffffff;
  --ink:#111111;
  --muted:#6b6b6b;
  --soft-grey:#f4f4f4;
  --blush:#fbece8;
  --line:#e2e2e2;
  --footer-text:#b9b9b9;
}
*{margin:0;padding:0;box-sizing:border-box}
html,body{width:1200px;height:4272px;overflow:hidden}
body{position:relative;font-family:"Montserrat",sans-serif;color:var(--ink);background:var(--white)}
.abs{position:absolute}
h1,h2,h3,.display{font-family:"Poppins",sans-serif}
.btn{position:absolute;background:var(--orange);color:var(--white);font-family:"Montserrat",sans-serif;font-weight:500;font-size:15px;display:flex;align-items:center;justify-content:center;letter-spacing:.3px}

/* top bar */
.topbar{left:0;top:0;width:1200px;height:43px;background:var(--black);color:var(--white);font-size:11px}
.topbar .item{position:absolute;top:0;height:43px;display:flex;align-items:center;gap:8px}

/* header */
.header{left:0;top:43px;width:1200px;height:98px;background:var(--white)}
.brand{position:absolute;display:flex;align-items:center;gap:10px;font-family:"Montserrat",sans-serif;font-weight:600;font-size:24px;white-space:nowrap}
.brand .mark{width:14px;height:14px;background:var(--orange)}
.header .brand{left:45px;top:34px;color:var(--ink)}
.nav a{position:absolute;top:42px;font-family:"Poppins",sans-serif;font-size:15px;font-weight:500;color:var(--ink);text-decoration:none}

/* hero */
.hero{left:3px;top:141px;width:1189px;height:514px;background:linear-gradient(180deg,#5c5f63 0%,#3e4146 55%,#2b2d31 100%)}
.hero h1{position:absolute;left:52px;top:78px;font-size:50px;line-height:59px;font-weight:700;color:var(--white)}
.hero p{position:absolute;left:52px;top:268px;width:420px;font-size:15.5px;line-height:19px;color:var(--white)}

/* features */
.band-grey{left:0;top:655px;width:1200px;height:811px;background:var(--soft-grey)}
.roof{position:absolute;top:600px;width:0;height:0;border-left:80px solid transparent;border-right:80px solid transparent;border-bottom:56px solid var(--orange)}
.feature{position:absolute;top:655px;width:328px;height:210px;background:var(--white);border:1px solid var(--line);border-top:3px solid var(--orange)}
.feature.dark{background:var(--black);border-color:var(--black);border-top-color:var(--orange)}
.feature .icon{position:absolute;left:27px;top:-3px;width:125px;height:97px;background:var(--orange);display:flex;align-items:center;justify-content:center}
.feature h3{position:absolute;left:181px;top:28px;font-size:22px;line-height:27px;font-weight:600}
.feature p{position:absolute;left:27px;top:113px;width:280px;font-size:12.5px;line-height:16px;color:var(--muted)}
.feature .more{position:absolute;left:27px;top:182px;font-size:8.5px;font-weight:700;letter-spacing:.3px}
.feature.dark h3,.feature.dark .more{color:var(--white)}
.feature.dark p{color:#d6d6d6}

/* about */
.about-photo{left:80px;top:972px;width:336px;height:336px;border-radius:50%;border:2px solid var(--orange);background:linear-gradient(160deg,#9fb4b0,#5f6e6c 60%,#3a3f3f)}
.badge{left:279px;top:1248px;width:226px;height:104px;background:var(--orange);border:4px solid var(--white);border-radius:4px;box-shadow:0 6px 18px rgba(0,0,0,.12);color:var(--white);display:flex;align-items:center;gap:14px;padding-left:14px}
.badge .num{font-family:"Poppins",sans-serif;font-size:54px;font-weight:600}
.badge .label{font-size:15px;line-height:18px}
.about h2{position:absolute;left:588px;top:1000px;font-size:44px;line-height:54px;font-weight:700}
.about p{position:absolute;left:588px;top:1132px;width:520px;font-size:13.3px;line-height:24px;color:var(--muted)}

/* section titles */
.section-title{position:absolute;left:0;width:1200px;text-align:center;font-size:44px;font-weight:700}

/* services */
.services{left:0;top:1466px;width:1200px;height:791px;background:var(--blush)}
.service{position:absolute;width:260px;height:246px;overflow:hidden}
.service .label{position:absolute;left:20px;bottom:26px;font-family:"Poppins",sans-serif;font-size:28px;line-height:37px;color:var(--white);font-weight:400}
.service .label::after{content:"";display:block;width:140px;height:3px;background:var(--orange);margin-top:2px}
.service.active{background:#cf6a49;padding:6px}
.service.active .frame{position:absolute;left:6px;top:6px;right:6px;bottom:6px;border:3px solid var(--white)}
.service.active .title{position:absolute;left:30px;top:16px;font-family:"Poppins",sans-serif;font-size:28px;line-height:37px;color:var(--white)}
.service.active p{position:absolute;left:30px;top:118px;width:210px;font-size:12.5px;line-height:22px;color:#fde7dc}
.service.active .mini{position:absolute;left:30px;top:198px;width:96px;height:16px;background:var(--orange);color:var(--white);font-size:7px;font-weight:600;display:flex;align-items:center;justify-content:center}

/* projects */
.project{position:absolute;top:2432px;width:268px;height:401px;background:var(--white);border:1px solid var(--line)}
.project .photo{position:absolute;left:0;top:0;width:266px;height:230px}
.project .date{position:absolute;right:0;top:192px;width:88px;height:76px;background:var(--orange);color:var(--white);font-size:14px;line-height:20px;text-align:center;display:flex;align-items:center;justify-content:center}
.project h3{position:absolute;left:15px;top:284px;font-size:26px;font-weight:500}
.project p{position:absolute;left:15px;top:328px;width:220px;font-size:12px;line-height:15px;color:var(--muted)}
.project .more{position:absolute;left:15px;top:372px;font-size:12px;color:var(--orange);font-weight:500}

/* gallery */
.gallery{left:0;top:2875px;width:1200px;height:817px;background:var(--blush)}
.shot{position:absolute;border-radius:12px}

/* footer */
.footer{left:0;top:3692px;width:1200px;height:580px;background:var(--black);color:var(--white)}
.footer .brand{left:57px;top:76px;color:var(--white)}
.social{position:absolute;top:80px;width:44px;height:38px;border:1px solid #3a3a3a;background:#1a1a1a;display:flex;align-items:center;justify-content:center}
.social span{width:12px;height:12px;background:#d0d0d0;border-radius:2px}
.footer .rule{position:absolute;left:0;top:170px;width:1200px;height:1px;background:#222}
.col h4{position:absolute;font-family:"Poppins",sans-serif;font-size:21px;font-weight:600}
.col .bar{position:absolute;width:46px;height:3px;background:var(--orange)}
.links li{position:absolute;list-style:none;font-size:14px;color:var(--footer-text);padding-left:22px}
.links li::before{content:"";position:absolute;left:0;top:5px;width:6px;height:6px;border-right:1.5px solid var(--footer-text);border-top:1.5px solid var(--footer-text);transform:rotate(45deg)}
.hours div{position:absolute;left:917px;font-size:14.5px;color:var(--footer-text)}
.hours b{color:var(--white);font-weight:600}
</style>
</head>
<body>

<!-- top bar -->
<div class="abs topbar">
  <div class="item" style="left:40px">
    <svg width="16" height="16" viewBox="0 0 16 16"><circle cx="8" cy="8" r="8" fill="#f26522"/><path d="M8 4v4.5l3 1.8" stroke="#fff" stroke-width="1.6" fill="none" stroke-linecap="round"/></svg>
    <span>Mon to Sat: 09:00 am to 05:00 pm</span>
  </div>
  <div class="item" style="left:282px">
    <svg width="22" height="15" viewBox="0 0 22 15"><rect width="22" height="15" rx="1.5" fill="#f26522"/><path d="M1.5 1.5l9.5 7 9.5-7" stroke="#fff" stroke-width="1.5" fill="none"/></svg>
    <span>hello@brelroofing.example</span>
  </div>
</div>

<!-- header -->
<header class="abs header">
  <div class="brand"><span class="mark"></span>Brel Roofing</div>
  <nav class="nav">
    <a style="left:305px">HOME</a>
    <a style="left:392px">ABOUT US</a>
    <a style="left:518px">SERVICES</a>
    <a style="left:640px">GALLERY</a>
    <a style="left:757px">CONTACT</a>
  </nav>
  <div class="btn" style="left:952px;top:32px;width:188px;height:38px">GET A QUOTE</div>
</header>

<!-- hero -->
<section class="abs hero" role="img" aria-label="New York City skyline seen from a commercial flat rooftop with skylights">
  <h1>Professional &amp;<br>Affordable<br>Roofing Services.</h1>
  <p>We provide a variety of roofing and maintenance services for all type of house makes happy.</p>
  <div class="btn" style="left:52px;top:339px;width:188px;height:36px">GET A QUOTE</div>
</section>

<!-- features -->
<div class="abs band-grey"></div>
<div class="roof" style="left:72px"></div>
<div class="roof" style="left:445px"></div>
<div class="roof" style="left:820px"></div>

<div class="feature" style="left:62px">
  <div class="icon"><svg width="72" height="62" viewBox="0 0 72 62" fill="none" stroke="#fff" stroke-width="2"><path d="M6 40l24-14 30 18-24 14z"/><path d="M14 35l30 18M22 31l30 18M18 44l24-14"/><circle cx="48" cy="16" r="11"/><path d="M56 24l8 8"/></svg></div>
  <h3>Perfect<br>Installs</h3>
  <p>Nullam neque augue, maximus id nulla id, dignissim tristique nunc.</p>
  <div class="more">READ MORE</div>
</div>
<div class="feature dark" style="left:430px">
  <div class="icon"><svg width="72" height="62" viewBox="0 0 72 62" fill="none" stroke="#fff" stroke-width="2"><path d="M10 24l26-14 26 14"/><rect x="12" y="26" width="48" height="26"/><path d="M12 34h48M12 42h48M24 26v26M36 26v26M48 26v26"/></svg></div>
  <h3>Reliable<br>Upgrades</h3>
  <p>Nullam neque augue, maximus id nulla id, dignissim tristique nunc.</p>
  <div class="more">READ MORE</div>
</div>
<div class="feature" style="left:800px">
  <div class="icon"><svg width="72" height="62" viewBox="0 0 72 62" fill="none" stroke="#fff" stroke-width="2"><path d="M34 8h30M34 18h30M34 28h30M34 38h30M34 48h30"/><path d="M14 54l6-30 12 8M20 24l-6-8"/><circle cx="14" cy="12" r="4"/></svg></div>
  <h3>Upkeep<br>&amp; Repair</h3>
  <p>Nullam neque augue, maximus id nulla id, dignissim tristique nunc.</p>
  <div class="more">READ MORE</div>
</div>

<!-- about -->
<section class="about">
  <div class="abs about-photo" role="img" aria-label="Roofer's gloved hands fixing a flat roof panel"></div>
  <div class="abs badge"><span class="num">10+</span><span class="label">Years Of<br>Experience</span></div>
  <h2>Trusted and Reputable<br>Roofing Company</h2>
  <p>we are a trusted and reputable roofing company specializing in new construction flat roof installation and repair. With years of experience in the industry, we take pride in providing exceptional roofing solutions to our valued clients. Our team of highly skilled and dedicated roofing professionals understands the unique challenges and requirements of new construction projects.</p>
  <div class="btn" style="left:588px;top:1308px;width:187px;height:39px">GET A QUOTE</div>
</section>

<!-- services -->
<section class="abs services">
  <h2 class="section-title" style="top:42px">Our Services</h2>
  <div class="service" style="left:122px;top:162px;background:linear-gradient(180deg,#8e9aa3,#7c6a52 55%,#4d5152)" role="img" aria-label="Mountain town with flat roofs">
    <div class="label">Flat Roof<br>Installation</div>
  </div>
  <div class="service active" style="left:446px;top:162px">
    <div class="frame"></div>
    <div class="title">Roof Leak<br>Repairs</div>
    <p>Nulla commodo dolor massa, vel pellentesque nulla congue quis.</p>
    <div class="mini">READ MORE</div>
  </div>
  <div class="service" style="left:793px;top:162px;background:linear-gradient(160deg,#9fb2ae,#5d6969 60%,#3d4242)" role="img" aria-label="Roofer working on flashing">
    <div class="label">Flashing<br>Services</div>
  </div>
  <div class="service" style="left:122px;top:474px;background:linear-gradient(180deg,#8d8a88,#7a6a5f 60%,#8d8f91)" role="img" aria-label="Worker on corrugated commercial roof">
    <div class="label">Commercial<br>Services</div>
  </div>
  <div class="service" style="left:446px;top:474px;background:linear-gradient(160deg,#b07a5a,#5b6f86 55%,#54585c)" role="img" aria-label="Roofers in hard hats waterproofing">
    <div class="label">Water<br>Proofing</div>
  </div>
  <div class="service" style="left:793px;top:474px;background:linear-gradient(180deg,#676a6c,#8a8c8e 60%,#5c5e60)" role="img" aria-label="Metal residential roof">
    <div class="label">Residential<br>Services</div>
  </div>
</section>

<!-- projects -->
<h2 class="section-title" style="top:2318px">Our Recent Projects</h2>
<div class="project" style="left:137px">
  <div class="photo" role="img" aria-label="Roofer fixing flat roof panel" style="background:linear-gradient(160deg,#a4b8b3,#5d6a69 60%,#3b4040)"></div>
  <div class="date">APR 19<br>2023</div>
  <h3>ROOF REPAIR</h3>
  <p>Roof ake type specimen book survived notte five centuriesIso</p>
  <div class="more">Read More</div>
</div>
<div class="project" style="left:454px">
  <div class="photo" role="img" aria-label="Flat rooftops overlooking mountains" style="background:linear-gradient(180deg,#909ca4,#7d6b52 50%,#595d60)"></div>
  <div class="date">APR 19<br>2023</div>
  <h3>ROOF REPAIR</h3>
  <p>Roof ake type specimen book survived notte five centuriesIso</p>
  <div class="more">Read More</div>
</div>
<div class="project" style="left:770px">
  <div class="photo" role="img" aria-label="Workers rolling membrane on a flat roof" style="background:linear-gradient(170deg,#6d7f90,#2f4f7d 55%,#243e66)"></div>
  <div class="date">APR 19<br>2023</div>
  <h3>ROOF REPAIR</h3>
  <p>Roof ake type specimen book survived notte five centuriesIso</p>
  <div class="more">Read More</div>
</div>

<!-- gallery -->
<section class="abs gallery">
  <h2 class="section-title" style="top:60px">Photo Gallery</h2>
  <div class="shot" style="left:192px;top:193px;width:220px;height:395px;background:linear-gradient(180deg,#a2a7ab,#3c3e42 60%,#2a2b2e)" role="img" aria-label="City skyscrapers"></div>
  <div class="shot" style="left:465px;top:193px;width:220px;height:185px;background:linear-gradient(160deg,#8c8c8a,#5d5a56 50%,#3d4a63)" role="img" aria-label="Gloved hands laying shingles"></div>
  <div class="shot" style="left:465px;top:405px;width:220px;height:183px;background:linear-gradient(180deg,#e6e4e0,#2e6a52 45%,#5c5f62)" role="img" aria-label="Worker rolling roofing membrane"></div>
  <div class="shot" style="left:733px;top:193px;width:220px;height:395px;background:linear-gradient(180deg,#c98b77,#9a8f88 45%,#c8ccd0)" role="img" aria-label="Metal roof against brick wall"></div>
  <div class="btn" style="left:482px;top:640px;width:188px;height:38px">VIEW MORE</div>
</section>

<!-- footer -->
<footer class="abs footer">
  <div class="brand"><span class="mark"></span>Brel Roofing</div>
  <svg class="abs" style="left:462px;top:78px" width="48" height="48" viewBox="0 0 48 48"><circle cx="24" cy="24" r="24" fill="#f26522"/><path d="M18 15c-2 1-3 3-2 6 2 5 6 9 11 11 3 1 5 0 6-2l-3-3-3 1c-2-1-5-4-6-6l1-3z" fill="#fff"/></svg>
  <div class="abs" style="left:524px;top:78px;font-size:15px">Need Any Roofing Help?</div>
  <div class="abs" style="left:524px;top:99px;font-size:22px;font-weight:700;font-family:'Montserrat',sans-serif">Call Us: +123-555-0147</div>
  <div class="social" style="left:910px" aria-label="Social link"><span></span></div>
  <div class="social" style="left:960px" aria-label="Social link"><span></span></div>
  <div class="social" style="left:1010px" aria-label="Social link"><span></span></div>
  <div class="social" style="left:1059px" aria-label="Social link"><span></span></div>
  <div class="social" style="left:1109px" aria-label="Social link"><span></span></div>
  <div class="rule"></div>

  <div class="col">
    <h4 style="left:45px;top:254px">Our Services</h4>
    <div class="bar" style="left:45px;top:298px"></div>
    <ul class="links">
      <li style="left:45px;top:340px">Damage Roofing</li>
      <li style="left:45px;top:377px">Roof Repair</li>
      <li style="left:45px;top:413px">Roof Renovation</li>
      <li style="left:222px;top:340px">Siding Corner</li>
      <li style="left:222px;top:377px">Roof Installation</li>
      <li style="left:222px;top:413px">Roof Animation</li>
    </ul>
  </div>

  <div class="col">
    <h4 style="left:481px;top:254px">Newsletter</h4>
    <div class="bar" style="left:481px;top:298px"></div>
    <div class="abs" style="left:481px;top:337px;width:270px;font-size:14px;line-height:24px;color:var(--footer-text)">Subscribe For Daily Latest News &amp; Updates</div>
    <div class="abs" style="left:481px;top:416px;width:310px;height:44px;background:#2b2b2b;font-size:14px;color:#cfcfcf;display:flex;align-items:center;padding-left:28px">Your email address</div>
    <div class="btn" style="left:481px;top:468px;width:310px;height:42px;font-size:14px">Subscribe Now</div>
  </div>

  <div class="col hours">
    <h4 style="left:917px;top:254px">Working Hours</h4>
    <div class="bar" style="left:917px;top:298px"></div>
    <div style="top:340px"><b>Monday:</b> 10.00AM - 4.00PM</div>
    <div style="top:379px"><b>Tuesday:</b> 10.00AM - 4.00PM</div>
    <div style="top:418px"><b>Wednesday:</b> 10.00AM - 4.00PM</div>
    <div style="top:457px"><b>Thursday:</b> 10.00AM - 4.00PM</div>
    <div style="top:496px"><b>Friday:</b> Close</div>
  </div>
</footer>

</body>
</html>
```